Packaging box designs for Hollister Forge, a series of five designs for automotive parts

We need a series of five packaging box designs for an a start up in Orange County CA named "Hollister Forge". Winner will be contracted for future product design. We are an remanufactured autoparts wholesaler focusing on five product lines: Starters, Alternators, Engine Control Units (ECU), Transmission Control Units (TCU), and Transmission Valvebodies. We would like the designer to design a series of packaging boxes with the same theme for each of the product lines. This series of remanufactured products will be marketed under the "Hollister Renew" trademark (logo attached). We want a clean and simple design theme that reflect environmental consciousness and technology/precision. We would like the primary color of our company to be used on the design (blue and white). We would like to include the company logo, the product name, and a blueprint schematic of the product (if possible, doesn't have to be exact, general schematic outline would do). Beyond that, a minimalist approach is preferred. For each product box, there will be six faces on the exterior available for design, with the possibility of one of the interior face (though not all faces need to have features). All five product boxes should carry the same over all theme, design layout, color and font choices to ensure consistent brand identity. All designs will be printed on roll end tuck top (RETT) mailer boxes (sample box drawing included, box dimensions are not accurate in sample and differ from product to product). Sample pictures of each products are attached for reference.

Target Market(s)

Mechanics, autoparts retailer, autoparts wholesaler, autoparts rebuilders.

Industry/Entity Type

Automotive

Requirements
Must have
• Company logo, trademark name (Hollister Renew), name of product (starter, alternator, etc)
Nice to have
• We like a design style similar to that of Zelvo accessories, where the box is plain white with a simple view of the product displayed. If possible, we'd like the display to be in some kind of blueprint schematic format. If designer could incorporate the company and trademark color scheme it would be a plus.

```html
<!DOCTYPE html>
<html lang="en">
<head>
<meta charset="utf-8">
<title>Hollister Forge – Replacement Parts Packaging</title>
<link href="https://fonts.googleapis.com/css2?family=Raleway:wght@300;400;600;700&display=swap" rel="stylesheet">
<style>
  :root {
    --bg-light: #4a4a4a;
    --bg-dark: #161616;
    --brand-blue: #1aa3e0;
    --ink: #2f2f33;
    --ink-soft: #8a8a90;
    --ink-strong: #55555c;
    --panel-top: #f7f7f9;
    --panel-bottom: #e3e4e8;
    --band-grey: #d3d5dc;
    --white: #ffffff;
  }
  * { box-sizing: border-box; margin: 0; padding: 0; }
  html, body { width: 715px; height: 1200px; overflow: hidden; }
  body {
    background: radial-gradient(ellipse at 50% 55%, var(--bg-light) 0%, var(--bg-dark) 75%);
    font-family: "Raleway", sans-serif;
    position: relative;
  }

  /* Page header */
  .brand-header {
    position: absolute; top: 92px; left: 0; width: 100%;
    display: flex; align-items: center; justify-content: center; gap: 16px;
  }
  .brand-header .mark { width: 30px; height: 30px; background: var(--brand-blue); }
  .brand-header .name { color: var(--white); font-weight: 700; font-size: 30px; letter-spacing: 1px; }

  /* Shared panel styles */
  .panel {
    position: absolute; overflow: hidden;
    background: linear-gradient(180deg, var(--panel-top), var(--panel-bottom));
    box-shadow: 0 8px 20px rgba(0,0,0,0.55);
  }
  .panel .lines { position: absolute; inset: 0; }
  .panel .grey-band { fill: var(--band-grey); opacity: 0.65; }
  .panel .blue-line { fill: none; stroke: var(--brand-blue); stroke-width: 5; }
  .panel > *:not(.lines) { position: absolute; }
  .title { font-weight: 300; color: var(--ink); line-height: 1; white-space: nowrap; }
  .subtitle { font-weight: 400; color: var(--brand-blue); text-transform: uppercase; white-space: nowrap; }
  .schematic {
    border-radius: 14px;
    background: radial-gradient(circle at 50% 50%, #c4c5cb 0%, #d8d9de 55%, rgba(227,228,232,0) 78%);
  }
  .tagline { font-weight: 300; color: var(--ink-soft); text-transform: uppercase; line-height: 1.3; white-space: nowrap; }
  .tagline strong { font-weight: 600; color: var(--ink-strong); }
  .face-brand { display: flex; align-items: center; gap: 5px; }
  .face-brand .mark { background: var(--brand-blue); }
  .face-brand .name { font-weight: 600; color: var(--ink); text-transform: uppercase; white-space: nowrap; }

  /* Starter box */
  .starter-end { left: 40px; top: 315px; width: 62px; height: 185px; }
  .starter-end .face-brand { left: 6px; top: 70px; flex-direction: column; gap: 6px; }
  .starter-end .mark { width: 14px; height: 14px; }
  .starter-end .name { font-size: 6px; }
  .starter-front { left: 102px; top: 315px; width: 258px; height: 185px; }
  .starter-front .title { left: 80px; top: 14px; font-size: 30px; }
  .starter-front .subtitle { left: 82px; top: 46px; font-size: 7px; }
  .starter-front .schematic { left: 128px; top: 58px; width: 120px; height: 92px; }
  .starter-front .tagline { left: 36px; top: 98px; font-size: 10px; }
  .starter-front .face-brand { right: 12px; bottom: 12px; }
  .starter-front .mark { width: 9px; height: 9px; }
  .starter-front .name { font-size: 6px; }

  /* Small alternator box */
  .alt-small { left: 395px; top: 250px; width: 280px; height: 200px; }
  .alt-small .title { left: 16px; top: 18px; font-size: 31px; }
  .alt-small .subtitle { left: 17px; top: 50px; font-size: 7.5px; }
  .alt-small .schematic { left: 130px; top: 66px; width: 130px; height: 100px; }
  .alt-small .tagline { left: 20px; top: 114px; font-size: 10px; }
  .alt-small .face-brand { right: 16px; bottom: 12px; }
  .alt-small .mark { width: 10px; height: 10px; }
  .alt-small .name { font-size: 6px; }

  /* Large alternator box: top, front, side */
  .alt-top { left: 40px; top: 640px; width: 405px; height: 155px; }
  .alt-top .title { left: 90px; top: 30px; font-size: 40px; }
  .alt-top .subtitle { left: 120px; top: 74px; font-size: 10px; }
  .alt-top .face-brand { left: 130px; top: 112px; }
  .alt-top .mark { width: 12px; height: 12px; }
  .alt-top .name { font-size: 8px; }

  .alt-front { left: 40px; top: 800px; width: 405px; height: 335px; }
  .alt-front .title { left: 18px; top: 22px; font-size: 56px; }
  .alt-front .subtitle { left: 22px; top: 86px; font-size: 14px; }
  .alt-front .schematic { left: 180px; top: 140px; width: 200px; height: 160px; }
  .alt-front .tagline { left: 30px; top: 184px; font-size: 16px; }
  .alt-front .face-brand { right: 22px; bottom: 18px; }
  .alt-front .mark { width: 20px; height: 20px; }
  .alt-front .name { font-size: 11px; }

  .alt-side { left: 450px; top: 800px; width: 225px; height: 335px; }
  .alt-side .title { left: 16px; top: 20px; font-size: 29px; }
  .alt-side .subtitle { left: 17px; top: 54px; font-size: 7.5px; }
  .alt-side .info-frame {
    left: 16px; top: 84px; width: 193px; height: 228px;
    border: 1.5px solid var(--brand-blue);
    padding: 20px 16px;
    font-size: 11px; line-height: 1.5; color: var(--ink); text-transform: uppercase;
  }
  .alt-side .info-frame .face-brand { position: absolute; left: 16px; bottom: 16px; }
  .alt-side .mark { width: 12px; height: 12px; }
  .alt-side .name { font-size: 8px; }
</style>
</head>
<body>

  <header class="brand-header">
    <span class="mark"></span>
    <span class="name">HOLLISTER FORGE</span>
  </header>

  <!-- Starter box -->
  <section class="panel starter-end">
    <div class="face-brand"><span class="mark"></span><span class="name">Hollister Forge</span></div>
  </section>
  <section class="panel starter-front">
    <svg class="lines" width="258" height="185" viewBox="0 0 258 185">
      <polygon class="grey-band" points="0,122 150,122 168,140 258,140 258,156 160,156 142,138 0,138"/>
      <polyline class="blue-line" points="0,176 100,176 120,150 258,150"/>
      <polyline class="blue-line" points="140,66 225,66 245,90 258,90"/>
    </svg>
    <h2 class="title">STARTER</h2>
    <p class="subtitle">Arranque, Démarreur</p>
    <div class="schematic" role="img" aria-label="Line schematic drawing of a starter motor"></div>
    <p class="tagline">Replacement<br>Part<br><strong>Best Quality</strong></p>
    <div class="face-brand"><span class="mark"></span><span class="name">Hollister Forge</span></div>
  </section>

  <!-- Small alternator box -->
  <section class="panel alt-small">
    <svg class="lines" width="280" height="200" viewBox="0 0 280 200">
      <polygon class="grey-band" points="0,150 120,150 140,170 280,170 280,186 132,186 112,166 0,166"/>
      <polyline class="blue-line" points="0,84 60,84 80,102 280,102"/>
      <polyline class="blue-line" points="230,160 280,160"/>
    </svg>
    <h2 class="title">ALTERNATOR</h2>
    <p class="subtitle">Alternador, Alternateur</p>
    <div class="schematic" role="img" aria-label="Line schematic drawing of an alternator"></div>
    <p class="tagline">Replacement<br>Part<br><strong>Best Quality</strong></p>
    <div class="face-brand"><span class="mark"></span><span class="name">Hollister Forge</span></div>
  </section>

  <!-- Large alternator box: top panel -->
  <section class="panel alt-top">
    <svg class="lines" width="405" height="155" viewBox="0 0 405 155">
      <polygon class="grey-band" points="0,14 150,14 170,30 405,30 405,44 162,44 142,28 0,28"/>
      <polygon class="grey-band" points="0,96 180,96 200,116 405,116 405,130 192,130 172,110 0,110"/>
    </svg>
    <h2 class="title">ALTERNATOR</h2>
    <p class="subtitle">Alternador, Alternateur</p>
    <div class="face-brand"><span class="mark"></span><span class="name">Hollister Forge</span></div>
  </section>

  <!-- Large alternator box: front panel -->
  <section class="panel alt-front">
    <svg class="lines" width="405" height="335" viewBox="0 0 405 335">
      <polygon class="grey-band" points="0,160 160,160 182,182 405,182 405,200 174,200 152,178 0,178"/>
      <polyline class="blue-line" points="0,124 95,124 122,152 210,152"/>
      <polyline class="blue-line" points="300,280 405,280"/>
    </svg>
    <h2 class="title">ALTERNATOR</h2>
    <p class="subtitle">Alternador, Alternateur</p>
    <div class="schematic" role="img" aria-label="Line schematic drawing of an alternator"></div>
    <p class="tagline">Replacement<br>Part<br><strong>Best Quality</strong></p>
    <div class="face-brand"><span class="mark"></span><span class="name">Hollister Forge</span></div>
  </section>

  <!-- Large alternator box: side panel -->
  <section class="panel alt-side">
    <h2 class="title">ALTERNATOR</h2>
    <p class="subtitle">Alternador, Alternateur</p>
    <div class="info-frame">
      <p>Remanufactured to original specifications under the Hollister Renew program.</p>
      <div class="face-brand"><span class="mark"></span><span class="name">Hollister Forge</span></div>
    </div>
  </section>

</body>
</html>
```